Company letter head

Hello,
We are a global logistics company requiring a letterhead design for all our company documentation.
Company Name: Clearly display the full name of your company at the top of the letterhead.
Logo: Include your company logo for brand recognition.
Contact Information: This includes your company's address, phone number, email address, and website URL.
Target Market(s)
Clients/customers
Industry/Entity Type
Logistics
Font styles to use
Sans Serif
Requirements
Must have
- Company name and logo
Nice to have
- borders, header/footers

```html
<!DOCTYPE html>
<html lang="en">
<head>
<meta charset="utf-8">
<title>Northway Freight Lines – Letterhead</title>
<link href="https://fonts.googleapis.com/css2?family=Arimo:wght@400;700&family=Source+Sans+3:wght@400&display=swap" rel="stylesheet">
<style>
  :root{
    --backdrop:#d3d3d3;
    --paper:#ffffff;
    --ink:#4d4d4f;
    --ink-dark:#404041;
    --brand-red:#d41f26;
    --rule:#9a9a9a;
  }
  *{margin:0;padding:0;box-sizing:border-box}
  html,body{width:899px;height:1200px;overflow:hidden;background:var(--backdrop)}
  .letterhead{
    position:absolute;left:132px;top:152px;width:634px;height:897px;
    background:var(--paper);
    box-shadow:2px 3px 4px rgba(0,0,0,.35);
    font-family:"Arimo",Arial,sans-serif;color:var(--ink);
  }
  .brand{position:absolute;left:54px;top:60px;display:flex;align-items:center;gap:7px}
  .brand-mark{width:14px;height:14px;background:var(--brand-red)}
  .brand-name{font-family:"Arimo",Arial,sans-serif;font-weight:700;font-size:17px;color:var(--ink-dark);letter-spacing:.2px}
  .contact{position:absolute;left:463px;top:43px;font-size:10.4px;line-height:12.6px}
  .contact .address{margin-bottom:4px}
  .contact-row{display:flex;align-items:center;gap:4px}
  .contact-row svg{width:8px;height:8px;flex:none}
  .header-rule{position:absolute;left:54px;top:116px;width:527px;height:1px;background:var(--rule)}
  .salutation{position:absolute;left:58px;top:262px;font-family:"Source Sans 3",sans-serif;font-size:14.2px;color:var(--ink)}
  .body{position:absolute;left:57px;top:305px;width:530px;font-size:11.1px;line-height:13px}
  .body p{margin-bottom:11.5px;white-space:nowrap}
  .closing{position:absolute;left:58px;top:572px;font-family:"Source Sans 3",sans-serif;font-size:7.8px}
  .signatory{position:absolute;left:57px;top:614px;font-family:"Source Sans 3",sans-serif;font-size:15.5px;letter-spacing:-.9px;color:var(--ink)}
  .footer-band{position:absolute;left:0;bottom:6px;width:634px;height:13px;display:block}
</style>
</head>
<body>
<main class="letterhead">
  <header>
    <div class="brand">
      <span class="brand-mark"></span>
      <span class="brand-name">Northway Freight Lines</span>
    </div>
    <address class="contact" style="font-style:normal">
      <div class="address">Your address, city<br>state, ZIP 0000</div>
      <div class="contact-row">
        <svg viewBox="0 0 10 10"><path d="M2 1l2 2-1 1.2c.6 1.2 1.5 2.1 2.8 2.8L7 6l2 2-1.4 1.5C4.5 9.3.7 5.5.5 2.4z" fill="var(--brand-red)"/></svg>
        <span>123-456-2100</span>
      </div>
      <div class="contact-row">
        <svg viewBox="0 0 10 10"><rect x="0" y="2" width="10" height="6.5" fill="var(--brand-red)"/><path d="M0 2l5 3.5L10 2" stroke="#fff" stroke-width=".8" fill="none"/></svg>
        <span>youremail@mailbox.com</span>
      </div>
      <div class="contact-row">
        <svg viewBox="0 0 10 10"><circle cx="5" cy="5" r="4.6" fill="var(--brand-red)"/><path d="M.6 5h8.8M5 .5v9M5 .5c-2.4 2.4-2.4 6.6 0 9M5 .5c2.4 2.4 2.4 6.6 0 9" stroke="#fff" stroke-width=".6" fill="none"/></svg>
        <span>www.yourwebsite.com</span>
      </div>
    </address>
    <div class="header-rule"></div>
  </header>

  <p class="salutation">Dear Mr. Hale,</p>

  <section class="body">
    <p>Lorem ipsum dolor sit amet, consectetuer adipiscing elit, sed diam nonmmy nibh euismod tincidunt ut laor<br>eet dolore magna aliquam erat volutpat. Ut wisi enim ad minim veniam, quis nostrud exerci tationmcorper<br>suscipit lobortis nisl ut aliquip ex ea commodo consequat. Duis autem vel eum iriure dolor in hendrerit in<br>vulputate velit esse molestie consequat, vel illum dolore eu feugiat</p>
    <p>Rorem ipsum dolor sit amet, consectetuer adipiscing elit, sed diam nonmmy nibh euismod tincidunt ut laor<br>eet dolore magna aliquam erat volutpat. Ut wisi enim ad minim veniam, quis nostrud exerci tationmcorper<br>suscipit lobortis nisl ut aliquip ex ea commodo consequat. Duis autem vel eum iriure dolor in hendrerit in<br>vulputate velit esse molest</p>
    <p>Dorem ipsum dolor sit amet, consectetuer adipiscing elit, sed diam nonmmy nibh euismod tincidunt ut laor<br>eet dolore magna aliquam erat volutpat. Ut wisi enim ad minim veniam, quis nostrud exerci tationmcorper<br>suscipit lobortis nisl ut aliquip ex ea commodo consequat. Duis autem vel eum iriure dolor in hendrerit in<br>suscipit lobortis nisl ut aliquip ex ea commodo consequat. Duis autem vel eum iriure dolor in hendrerit in<br>vulputate velit esse molestie consequat, vel illum</p>
    <p>Sorem ipsum dolor sit amet, consectetuer adipiscing elit, sed diam nonmmy nibh euismod tincidunt ut laor<br>eet dolore magna aliquam erat volutpat. Ut wisi enim ad minim veniam, quis nostrud exerci tationmcorper<br>suscipit lobortis nisl ut aliquip ex ea commodo consequat. Duis autem vel eum iriure dolor in</p>
  </section>

  <p class="closing">Sincerely,</p>
  <p class="signatory">Marten K. Oslund</p>

  <svg class="footer-band" viewBox="0 0 634 13" preserveAspectRatio="none" aria-hidden="true">
    <polygon points="0,0 464,0 453,13 0,13" fill="var(--brand-red)"/>
    <polygon points="475,0 634,0 634,13 464,13" fill="var(--ink-dark)"/>
  </svg>
</main>
</body>
</html>
```